New Business Card Design Project

Need a design that will create an impact / strong impression towards our clients for our business. We are in the lighting business and we do lighting retrofits for large commercial to industrial clientele.

Target Market(s)

Lighting Industry

Industry/Entity Type

Business

Other font styles liked:
• we would like to use the font on our logo, not sure what it is though..

Requirements
Must have
• Our logo.
Nice to have
• We are open to suggestions that have to do with lighting.

```html
<!DOCTYPE html>
<html lang="en">
<head>
<meta charset="utf-8">
<title>Brightway Retrofit Partners – Business Card</title>
<link rel="stylesheet" href="https://fonts.googleapis.com/css2?family=Montserrat:wght@400;500;600;700;800&display=swap">
<style>
  :root {
    --page: #2a2a2a;
    --green-light: #12c257;
    --green: #0c9a45;
    --green-deep: #087a35;
    --green-dark: #1f5e2e;
    --green-pale: #8fd6a0;
    --ink: #1f3a26;
    --grey: #6b6b6b;
    --white: #ffffff;
  }
  * { box-sizing: border-box; margin: 0; padding: 0; }
  html, body {
    width: 1200px; height: 900px; overflow: hidden;
    background: var(--page);
    font-family: "Montserrat", sans-serif;
  }
  .stage {
    width: 1200px; height: 900px;
    display: flex; flex-direction: column; align-items: center; justify-content: center;
    gap: 40px;
  }
  .card {
    width: 700px; height: 400px; position: relative; overflow: hidden;
    box-shadow: 0 10px 30px rgba(0,0,0,.45);
  }

  /* Front */
  .card-front {
    background: linear-gradient(120deg, var(--green-light) 0%, var(--green) 50%, var(--green-deep) 100%);
    color: var(--white);
  }
  .front-brand {
    position: absolute; left: 150px; top: 130px; width: 400px;
    text-align: center;
  }
  .front-name {
    display: flex; align-items: center; justify-content: center; gap: 14px;
    font-size: 38px; font-weight: 800; letter-spacing: 1px;
  }
  .brand-square { width: 22px; height: 22px; background: currentColor; }
  .front-rule { height: 2px; background: var(--white); margin: 14px 0 12px; opacity: .9; }
  .front-tag { font-size: 12px; font-weight: 600; letter-spacing: 2px; text-transform: uppercase; }
  .front-web {
    position: absolute; left: 0; right: 0; top: 285px; text-align: center;
    font-size: 15px; font-weight: 500; letter-spacing: 3px;
  }

  /* Back */
  .card-back { background: var(--white); }
  .back-brand {
    position: absolute; right: 56px; top: 40px; width: 300px; text-align: right;
  }
  .back-name {
    display: flex; align-items: center; justify-content: flex-end; gap: 10px;
    font-size: 30px; font-weight: 800; color: var(--green-deep); letter-spacing: .5px;
  }
  .back-name .brand-square { width: 18px; height: 18px; }
  .back-rule { height: 2px; background: var(--green-dark); margin-top: 12px; }
  .back-address {
    position: absolute; right: 56px; top: 150px; text-align: right;
    font-size: 15px; line-height: 1.35; color: var(--grey);
  }
  .accent-line {
    position: absolute; left: 240px; right: 56px; top: 228px; height: 3px;
    display: flex;
  }
  .accent-line span { flex: 1; }
  .accent-line span:nth-child(1) { background: var(--green-dark); }
  .accent-line span:nth-child(2) { background: var(--green); }
  .accent-line span:nth-child(3) { background: var(--green-light); }
  .accent-line span:nth-child(4) { background: var(--green-pale); }
  .accent-line span:nth-child(5) { background: var(--green); }
  .person { position: absolute; left: 40px; top: 186px; }
  .person-name { font-size: 20px; font-weight: 700; color: var(--ink); letter-spacing: .5px; }
  .person-role { font-size: 17px; font-weight: 500; color: var(--green); letter-spacing: .5px; }
  .contacts {
    position: absolute; left: 40px; top: 250px; list-style: none;
    font-size: 15px; color: var(--grey); line-height: 1.45;
  }
  .contacts li { display: flex; align-items: center; gap: 10px; }
  .contacts svg { width: 14px; height: 14px; fill: var(--ink); flex: none; }
</style>
</head>
<body>
<main class="stage">
  <section class="card card-front" aria-label="Card front">
    <div class="front-brand">
      <div class="front-name"><span>BRIGHTWAY</span><span class="brand-square"></span></div>
      <div class="front-rule"></div>
      <div class="front-tag">Brightway Retrofit Partners</div>
    </div>
    <div class="front-web">www.brightwayretrofit.com</div>
  </section>

  <section class="card card-back" aria-label="Card back">
    <div class="back-brand">
      <div class="back-name"><span>BRIGHTWAY</span><span class="brand-square"></span></div>
      <div class="back-rule"></div>
    </div>
    <address class="back-address" style="font-style:normal">
      1420 Harbor Ridge Road<br>
      Fairview, Oregon 97024<br>
      www.brightwayretrofit.com
    </address>
    <div class="person">
      <div class="person-name">DANIEL REYES</div>
      <div class="person-role">CEO/FOUNDER</div>
    </div>
    <div class="accent-line"><span></span><span></span><span></span><span></span><span></span></div>
    <ul class="contacts">
      <li><svg viewBox="0 0 16 16"><path d="M3 1h3l1.5 4-2 1.2a9 9 0 0 0 4.3 4.3L11 8.5l4 1.5v3a2 2 0 0 1-2 2A13 13 0 0 1 1 3a2 2 0 0 1 2-2z"/></svg>555 210 4471</li>
      <li><svg viewBox="0 0 16 16"><path d="M4 0h8a1 1 0 0 1 1 1v14a1 1 0 0 1-1 1H4a1 1 0 0 1-1-1V1a1 1 0 0 1 1-1zm1 2v10h6V2zm3 11a1 1 0 1 0 0 2 1 1 0 0 0 0-2z"/></svg>555 318 6602</li>
      <li><svg viewBox="0 0 16 16"><path d="M4 1h7v4H4zM2 6h12a1 1 0 0 1 1 1v6H1V7a1 1 0 0 1 1-1zm2 5v4h8v-4z"/></svg>555 407 1985</li>
      <li><svg viewBox="0 0 16 16"><path d="M1 3h14v10H1zm1.5 1.2V5l5.5 4 5.5-4v-.8z"/></svg>daniel@brightwayretrofit.com</li>
    </ul>
  </section>
</main>
</body>
</html>
```